Cyber Security Site Design (Products & Consulting)

I need my website redesigned to be engaging, clean, efficient and modern. My company (when its up and running) is going to be concentrated on two things: a few specific products for cyber security as well as cyber security consulting services. The background I bring to the field is having worked with small companies all the way to the largest government organizations and advising them on their security posture and how to improve it. We need the ability to add products and services easily.

For a sample product, you can use either Heron (http://www.heron-relay.example/) or Vorlant Greystone (https://www.vorlant.example/products/relay-hub-and-layered-access-portal).

It will replace https://talmerocharts.example/

Target Market(s)

Cyber Security professionals in all verticals

Coding

Coded - Design and coding required

Number of Pages Required

4 page

Font styles to use
Sans Serif

Colors
6b449b

Requirements
Must have
• Ability to easily modify
• Have main page
• Have product specific pages
• Have consulting services pages
• Have executive team information
• Clean, modern design
• Usage of the logo and its color scheme
Nice to have
• I like the idea of a left collapsed sidebar (so icons only) that can expand for text.
• I am also open to a very unique landing page, possibly a shape in the middle (hexagons maybe?) with each of the options there.
Should not have
• Nothing that looks like it came out of a hacker movie

```html
<!DOCTYPE html>
<html lang="en">
<head>
<meta charset="utf-8">
<title>Talmero Charts, LLC. — Cyber Security</title>
<link rel="stylesheet" href="https://fonts.googleapis.com/css2?family=Open+Sans:wght@400;600;700&family=Raleway:wght@400;500;600;700&display=swap">
<style>
:root{
  --purple:#6b449b;
  --purple-dark:#57357f;
  --topbar:#61656f;
  --hero:#0f3b4b;
  --hero-deep:#0a2a38;
  --ink:#1d1f2a;
  --body:#555a66;
  --muted:#8a8f99;
  --line:#e2e3e6;
  --soft:#f6f6f7;
  --white:#ffffff;
  --gold:#f2b01e;
  --footer:#0b0f2e;
  --footer-text:#aeb3c7;
  --btn-grey:#6c707b;
}
*{box-sizing:border-box;margin:0;padding:0}
html,body{width:1200px;height:3098px;overflow:hidden}
body{position:relative;background:var(--soft);font-family:"Open Sans",sans-serif;color:var(--body);font-size:14px}
.abs{position:absolute}
ul{list-style:none}

/* top bar */
.topbar{left:0;top:0;width:1200px;height:41px;background:var(--topbar);color:#e6e7ea;font-size:12px;display:flex;align-items:center;justify-content:space-between;padding:0 99px 0 112px}
.topbar .contact,.topbar .account{display:flex;gap:28px;align-items:center}
.topbar span{display:flex;align-items:center;gap:6px}

/* nav */
.nav{left:0;top:41px;width:1200px;height:89px;background:var(--white);display:flex;align-items:center;justify-content:space-between;padding:0 99px}
.brand{display:flex;align-items:center;gap:10px;font-family:"Raleway",sans-serif;font-weight:700;font-size:26px;color:var(--ink);letter-spacing:.5px}
.brand .mark{width:30px;height:30px;border-radius:50%;background:var(--purple)}
.menu{display:flex;gap:40px;font-family:"Raleway",sans-serif;font-weight:500;font-size:15px;color:var(--ink)}

/* hero */
.hero{left:0;top:130px;width:1200px;height:483px;background:linear-gradient(180deg,var(--hero) 0%,var(--hero-deep) 100%);text-align:center;color:var(--white)}
.hero h1{font-family:"Raleway",sans-serif;font-weight:400;font-size:40px;margin-top:135px}
.hero p{width:660px;margin:26px auto 0;font-size:12px;line-height:19px}
.hero .back{display:inline-block;margin-top:22px;font-size:13px;font-weight:600;border-bottom:1px solid var(--white);padding-bottom:2px}

/* pricing */
.plan{top:560px;width:316px;height:454px;background:var(--white);border:1px solid var(--line);text-align:center}
.plan h3{height:54px;line-height:54px;font-family:"Raleway",sans-serif;font-weight:700;font-size:19px;color:var(--ink);letter-spacing:.5px;border-bottom:1px solid var(--line)}
.plan .price{margin-top:50px;color:var(--purple);font-family:"Raleway",sans-serif;font-weight:700;font-size:34px}
.plan .price sup{font-size:15px;vertical-align:14px}
.plan .price small{font-size:15px}
.plan .per{font-size:16px;font-weight:600;color:var(--muted);margin-top:4px}
.plan ul{margin-top:22px;font-size:14px;font-weight:600;color:var(--muted);line-height:28px}
.btn-grey{display:inline-block;margin-top:28px;background:var(--btn-grey);color:var(--white);font-size:13px;font-weight:600;padding:13px 34px;border-radius:24px;box-shadow:0 10px 18px rgba(0,0,0,.22)}

/* help */
.help-copy{left:99px;top:1170px;width:480px}
.help-copy h2{font-family:"Raleway",sans-serif;font-weight:400;font-size:33px;color:var(--ink)}
.help-copy p{margin-top:18px;font-size:13px;line-height:25px}
.help-copy ul{margin-top:22px;font-size:13px;line-height:28px}
.help-copy li::before{content:"✓";color:var(--gold);font-weight:700;margin-right:14px}
.tile{width:224px;height:169px;border:1px solid #dcdde0;background:var(--soft);display:flex;flex-direction:column;align-items:center;justify-content:center;gap:22px;font-family:"Raleway",sans-serif;font-size:20px;color:var(--muted)}
.tile svg{width:30px;height:30px;stroke:#6d717a;fill:none;stroke-width:2}

/* feature */
.feature-bg{left:0;top:1640px;width:1200px;height:1458px;background:var(--white)}
.feature-photo{left:0;top:1664px;width:599px;height:430px;background:radial-gradient(circle at 62% 48%,#bfe6f0 0%,#3b8fa6 22%,#123b52 58%,#08182a 100%)}
.feature-copy{left:613px;top:1668px;width:490px}
.feature-copy .kicker{font-family:"Raleway",sans-serif;font-size:27px;color:var(--ink)}
.feature-copy h2{margin-top:8px;font-family:"Raleway",sans-serif;font-weight:700;font-size:34px;line-height:42px;color:var(--ink)}
.feature-copy p{margin-top:18px;font-size:13px;line-height:20px;color:var(--muted)}
.feature-copy ul{margin-top:16px;font-size:14px;line-height:27px;color:var(--body)}
.feature-copy li::before{content:"";display:inline-block;width:8px;height:8px;border:2px solid var(--gold);border-radius:50%;margin-right:14px;vertical-align:1px}

/* badges */
.badges{left:378px;top:2186px;display:flex;gap:44px;align-items:center}
.badge{height:40px;border-radius:6px;background:#e9eaec}

/* news */
.news{left:99px;top:2250px;width:1002px}
.news .label{font-family:"Raleway",sans-serif;font-size:26px;color:var(--ink)}
.news .headline{margin-top:14px;display:flex;align-items:center;gap:14px}
.news .date{background:var(--purple);color:var(--white);font-family:"Raleway",sans-serif;font-weight:700;font-size:26px;padding:3px 16px}
.news h2{font-family:"Raleway",sans-serif;font-weight:400;font-size:36px;color:var(--ink)}
.news p{margin-top:30px;font-size:13.5px;line-height:28px;color:var(--body)}
.btn-purple{left:525px;top:2480px;width:150px;height:43px;border-radius:22px;background:var(--purple);color:var(--white);font-size:13px;font-weight:700;display:flex;align-items:center;justify-content:center;box-shadow:0 12px 20px rgba(107,68,155,.35)}

/* footer */
.footer{left:0;top:2620px;width:1200px;height:478px;background:var(--footer);color:var(--footer-text);font-size:13px}
.fcol{top:98px;width:230px}
.fcol h4{font-family:"Open Sans",sans-serif;font-weight:700;font-size:16px;color:var(--white);margin-bottom:20px}
.fcol p{line-height:24px}
.fcol li{line-height:36px;border-bottom:1px solid rgba(255,255,255,.12)}
.social{display:flex;gap:8px;margin-top:46px}
.social span{width:18px;height:18px;background:#5b6ea8;border-radius:2px}
.field{height:42px;border:1px solid rgba(255,255,255,.2);margin-top:12px;padding:0 16px;line-height:40px;color:#6e738c}
.subscribe{margin-top:14px;height:40px;background:var(--purple);color:var(--white);font-weight:700;font-size:13px;display:flex;align-items:center;justify-content:center}
.copyright{left:99px;top:430px;font-size:13px}
.to-top{left:1070px;top:420px;width:30px;height:30px;border-radius:50%;background:var(--white);display:flex;align-items:center;justify-content:center}
</style>
</head>
<body>

<div class="abs topbar">
  <div class="contact">
    <span><svg width="12" height="12" viewBox="0 0 24 24" fill="#e6e7ea"><path d="M6.6 10.8a15 15 0 006.6 6.6l2.2-2.2c.3-.3.7-.4 1-.2 1.1.4 2.3.6 3.6.6.6 0 1 .4 1 1V20c0 .6-.4 1-1 1A17 17 0 013 4c0-.6.4-1 1-1h3.5c.6 0 1 .4 1 1 0 1.3.2 2.5.6 3.6.1.3 0 .7-.2 1z"/></svg>Phone:+15550142776</span>
    <span><svg width="13" height="11" viewBox="0 0 24 18" fill="none" stroke="#e6e7ea" stroke-width="2"><rect x="1" y="1" width="22" height="16"/><path d="M1 1l11 9 11-9"/></svg>someone@example.com</span>
  </div>
  <div class="account"><span>Account ▾</span><span>English ▾</span><span>Login</span><span>Register</span></div>
</div>

<header class="abs nav">
  <div class="brand"><span class="mark"></span>TALMERO</div>
  <nav class="menu"><span>Home</span><span>Our team ▾</span><span>Services</span><span>Products</span><span>Contact Us</span></nav>
</header>

<section class="abs hero" role="img" aria-label="Dark teal banner with a faint padlock and circuit backdrop">
  <h1>Talmero Charts, LLC.</h1>
  <p>Talmero Charts, LLC. is a company that takes its roots from the idea of providing appropriate and creative solutions for cyber security operations, development and management. We have a mission first mindset for our clients and their objectives.</p>
  <span class="back">⬅ Back Home</span>
</section>

<article class="abs plan" style="left:99px">
  <h3>CYBER SECURITY</h3>
  <div class="price"><sup>$</sup>180<small>.00</small></div>
  <div class="per">per year</div>
  <ul><li>Unlimited Storage</li><li>Free Domain Register</li><li>70FB Bandwidth</li><li>Free Panelry</li><li>24/7 instant Suport</li></ul>
  <span class="btn-grey">Get Started ›</span>
</article>
<article class="abs plan" style="left:442px">
  <h3>PRODUCTS</h3>
  <div class="price"><sup>$</sup>180<small>.00</small></div>
  <div class="per">per year</div>
  <ul><li>Unlimited Storage</li><li>Free Domain Register</li><li>70FB Bandwidth</li><li>Free Panelry</li><li>24/7 instant Suport</li></ul>
  <span class="btn-grey">Get Started ›</span>
</article>
<article class="abs plan" style="left:785px">
  <h3>SERVICES</h3>
  <div class="price"><sup>$</sup>180<small>.00</small></div>
  <div class="per">per year</div>
  <ul><li>Unlimited Storage</li><li>Free Domain Register</li><li>70FB Bandwidth</li><li>Free Panelry</li><li>24/7 instant Suport</li></ul>
  <span class="btn-grey">Get Started ›</span>
</article>

<section class="abs help-copy">
  <h2>How can we help today?</h2>
  <p>Lorem ipsum dolor sit amet, consectetur adipisicing elit, sed do eiusmod tempor incididunt ut labore et dolore magna aliqua. Ut enim ad minim veniam, quis nostrud exercitation ullamco laboris nisi ut aliquip ex ea commodo consequat. Duis aute irure dolor in reprehenderit in voluptate velit esse Cillumporro quisqua.</p>
  <ul>
    <li>dolor in reprehenderit in voluptate velit esse cillumporro quisqua.</li>
    <li>dolor in reprehenderit in voluptate velit esse cill.</li>
    <li>dolor in reprehenderit in volupta.</li>
  </ul>
</section>

<div class="abs tile" style="left:622px;top:1158px"><svg viewBox="0 0 24 24"><circle cx="12" cy="12" r="10"/><path d="M2 12h20M12 2c3 3 3 17 0 20M12 2c-3 3-3 17 0 20"/></svg>Cyber security</div>
<div class="abs tile" style="left:867px;top:1158px"><svg viewBox="0 0 24 24"><rect x="3" y="5" width="18" height="14" rx="2"/><path d="M3 13h18"/><circle cx="17" cy="16" r=".6"/></svg>Products</div>
<div class="abs tile" style="left:622px;top:1344px"><svg viewBox="0 0 24 24"><rect x="2" y="5" width="20" height="14" rx="2"/><path d="M2 10h20M6 15h5"/></svg>Services</div>
<div class="abs tile" style="left:867px;top:1344px"><svg viewBox="0 0 24 24"><rect x="2" y="4" width="20" height="16" rx="2"/><path d="M2 6l10 7 10-7"/></svg>Get Support</div>

<div class="abs feature-bg"></div>
<div class="abs feature-photo" role="img" aria-label="Photo of a server room aisle lit in blue and teal"></div>
<section class="abs feature-copy">
  <div class="kicker">Heron: Optimising Web Delivery</div>
  <h2>Heron is a caching proxy for the Web supporting HTTP, HTTPS, FTP</h2>
  <p>Heron is a caching proxy for the Web supporting HTTP, HTTPS, FTP, and more. It reduces bandwidth and improves response times by caching and reusing frequently-requested web pages.</p>
  <ul><li>Cyber security site &amp; design</li><li>Products</li><li>services</li></ul>
</section>

<div class="abs badges" aria-label="Partner certificates">
  <span class="badge" style="width:96px"></span>
  <span class="badge" style="width:56px;height:52px"></span>
  <span class="badge" style="width:90px"></span>
  <span class="badge" style="width:74px;height:34px"></span>
</div>

<section class="abs news">
  <div class="label">News</div>
  <div class="headline"><span class="date">May 28th</span><h2>Thank you for choosing us!</h2></div>
  <p>Heron is used by hundreds of Internet Providers world-wide to provide their users with the best possible web access. Heron optimises the data flow between client and server to improve performance and caches frequently-used content to save bandwidth. Heron can also route content requests to servers in a wide variety of ways to build cache server hierarchies which optimise network throughput. &gt; ...</p>
</section>
<div class="abs btn-purple">Read More »</div>

<footer class="abs footer">
  <div class="abs fcol" style="left:99px">
    <h4>About Us</h4>
    <p>Lorem ipsum dolor sit amet, consectetur adipiscing elit. Curabitur sollicitudin ultrices suscipit. Sed commodo vel mauris vel dapibus. Lorem ipsum dolor sit amet.</p>
    <div class="social"><span></span><span></span><span></span><span></span><span></span><span></span></div>
  </div>
  <div class="abs fcol" style="left:355px">
    <h4>Useful Links</h4>
    <ul><li>Home</li><li>About</li><li>Blog</li><li>Portfolio</li><li style="border:0">Contact</li></ul>
  </div>
  <div class="abs fcol" style="left:613px">
    <h4>Our Services</h4>
    <ul><li>Cyber security</li><li>secure internet</li><li>Dedicated Hosting</li><li>Hosting Features</li><li style="border:0">Domains Names</li></ul>
  </div>
  <div class="abs fcol" style="left:869px">
    <h4>News Letter</h4>
    <p style="border-bottom:1px solid rgba(255,255,255,.6);padding-bottom:6px">Lorem ipsum dolor sit amet,</p>
    <div class="field" style="margin-top:16px">Name</div>
    <div class="field">Email</div>
    <div class="subscribe">SUBSCRIBE</div>
  </div>
  <div class="abs copyright">Copyright © 2018 Cyber security site design. All Rights Reserved.</div>
  <div class="abs to-top"><svg width="12" height="12" viewBox="0 0 24 24" fill="none" stroke="#0b0f2e" stroke-width="3"><path d="M5 15l7-7 7 7"/></svg></div>
</footer>

</body>
</html>
```